"Corporal Birch" is a brand of gummied aids

Corporal Birch is a brand of service men gummies that help our heroes with anxiety, Irritability and hostility brought on by a condition known as PTSD.

I have uploaded example symbols that can be use to discribe the following
Caffeine-Free, No GMO, Sugar Free, Vegan,
Gluten Free, No THC, etc...

Looking for a label for an 8 or 10oz glass jar. The label needs to allow some view at the bottom of the jar to show the gummies.

My vision, and I welcome your, is a
silhouette of various service people saluting a, or various flags.

Each gummy is 15mg 60 count
Updates

I've decided to change the band name on the label. The project is a brand of Gummy aids for PTSD sufferers. The New Name: Valor Bites Target: All first responder service people wanting relief with no THC side affects.

Target Market(s)

All service people, Military, Police, Fire fighters, Medics, Nurses, Doctors, First Responders, etc... (Male and Females)

Font styles to use
Serif
Sans Serif

Requirements
Must have
• Correction: The service people don't have to be saluting a flag.
Note. My uploads are examples only.
Should not have
• Cartoons

```html
<!DOCTYPE html>
<html lang="en">
<head>
<meta charset="utf-8">
<title>Valor Bites – Gummy Label</title>
<link rel="stylesheet" href="https://fonts.googleapis.com/css2?family=Oswald:wght@600;700&family=Exo+2:wght@700;800&family=Roboto+Condensed:wght@400;700&display=swap">
<style>
  :root {
    --page: #f3fbfb;
    --label-light: #1f5f5b;
    --label-mid: #14423f;
    --label-dark: #0a2627;
    --mark-shade: #0f3835;
    --title-green: #c9efb2;
    --gold: #f2b733;
    --teal-text: #3cb9a6;
    --orange-text: #ea7d2c;
    --white-text: #f4f7f2;
    --pill: #0d2f2e;
  }
  * { box-sizing: border-box; margin: 0; padding: 0; }
  html, body { width: 1200px; height: 929px; overflow: hidden; background: var(--page); }
  .canvas { position: relative; width: 1200px; height: 929px; }

  .lid-label {
    position: absolute; left: 70px; top: 285px; width: 360px; height: 360px;
    border-radius: 50%;
    background: radial-gradient(circle at 50% 30%, var(--label-light), var(--label-mid) 55%, var(--label-dark));
    overflow: hidden; text-align: center;
  }
  .wrap-label {
    position: absolute; left: 490px; top: 240px; width: 640px; height: 450px;
    background: radial-gradient(ellipse at 50% 25%, var(--label-light), var(--label-mid) 50%, var(--label-dark));
    overflow: hidden;
  }

  .emblem-area { position: absolute; left: 50%; transform: translateX(-50%); border-radius: 50% 50% 40% 40%;
    background: radial-gradient(ellipse at 50% 45%, var(--mark-shade), rgba(15,56,53,0) 70%); }

  .brand-name { position: absolute; left: 0; right: 0; text-align: center;
    font-family: "Oswald", sans-serif; font-weight: 700; color: var(--title-green);
    line-height: .95; text-transform: uppercase; }
  .infused { position: absolute; left: 0; right: 0; text-align: center;
    font-family: "Exo 2", sans-serif; font-weight: 800; color: var(--gold); letter-spacing: 1px; }
  .claim { position: absolute; left: 0; right: 0; text-align: center;
    font-family: "Roboto Condensed", sans-serif; font-size: 12.5px; line-height: 1.1; color: var(--white-text); text-transform: uppercase; }
  .claim .stress { color: var(--teal-text); }
  .claim .anxiety { color: var(--gold); }
  .claim .irritability { color: var(--orange-text); }

  .dose-pill { position: absolute; left: 50%; transform: translateX(-50%);
    display: flex; align-items: center; gap: 8px; padding: 2px 12px; border-radius: 6px;
    background: var(--pill); white-space: nowrap; }
  .dose-pill .mg { font-family: "Exo 2", sans-serif; font-weight: 700; color: var(--teal-text); letter-spacing: 1px; }
  .dose-pill .divider { width: 1px; align-self: stretch; background: var(--label-light); }
  .dose-pill .count { font-family: "Oswald", sans-serif; font-weight: 700; color: var(--gold); }
  .dose-pill .count-label { font-family: "Roboto Condensed", sans-serif; font-weight: 700; color: var(--gold); line-height: .9; text-transform: uppercase; }

  .badge-column { position: absolute; top: 178px; display: flex; flex-direction: column; gap: 16px; }
  .badge-column.left { left: 62px; }
  .badge-column.right { right: 62px; }
  .badge { width: 50px; height: 50px; border-radius: 50%; border: 2px solid var(--gold);
    display: flex; align-items: center; justify-content: center; text-align: center;
    font-family: "Exo 2", sans-serif; font-weight: 700; font-size: 10px; line-height: 1; color: var(--gold); text-transform: uppercase; }
  .badge.plain { border-style: solid; }
  .badge svg { width: 24px; height: 24px; }
</style>
</head>
<body>
<main class="canvas">

  <section class="lid-label" aria-label="Lid label">
    <div class="dose-pill" style="top:28px">
      <span class="mg" style="font-size:17px">15MG</span>
      <span class="divider"></span>
      <span class="count" style="font-size:17px">60</span>
      <span class="count-label" style="font-size:8px">Gummy<br>Count</span>
    </div>
    <div class="emblem-area" role="img" aria-label="Dark teal spread-wing eagle silhouette" style="top:48px;width:210px;height:70px"></div>
    <h1 class="brand-name" style="top:112px;font-size:72px">Valor<br><span style="font-size:56px">Bites</span></h1>
    <p class="infused" style="top:272px;font-size:17px">CBD &amp; CBG INFUSED</p>
  </section>

  <section class="wrap-label" aria-label="Jar wrap label">
    <div class="emblem-area" role="img" aria-label="Dark teal spread-wing eagle silhouette" style="top:12px;width:290px;height:110px"></div>
    <h2 class="brand-name" style="top:96px;font-size:104px">Valor<br><span style="font-size:80px">Bites</span></h2>
    <p class="infused" style="top:292px;font-size:20px">CBD &amp; CBG INFUSED</p>
    <p class="claim" style="top:344px">
      Specially formulated to aid with<br>
      <span class="stress">Stress</span>, <span class="anxiety">Anxiety</span>, and <span class="irritability">Irritability</span>,<br>
      conditions associated with PTSD
    </p>
    <div class="dose-pill" style="top:402px">
      <span class="mg" style="font-size:20px">15MG</span>
      <span class="divider"></span>
      <span class="count" style="font-size:20px">60</span>
      <span class="count-label" style="font-size:9px">Gummy<br>Count</span>
    </div>

    <div class="badge-column left">
      <div class="badge">Non<br>GMO</div>
      <div class="badge">Sugar<br>Free</div>
      <div class="badge" style="font-size:9px">100%<br>Organic</div>
      <div class="badge">Gluten<br>Free</div>
    </div>
    <div class="badge-column right">
      <div class="badge plain" aria-label="Plant-based badge">
        <svg viewBox="0 0 24 24" aria-hidden="true"><path d="M12 3 C16 8 16 14 12 20 C8 14 8 8 12 3Z" fill="none" stroke="#f2b733" stroke-width="1.8"/><line x1="12" y1="8" x2="12" y2="22" stroke="#f2b733" stroke-width="1.5"/></svg>
      </div>
      <div class="badge" style="font-size:9px">Caffeine<br>Free</div>
      <div class="badge">Vegan</div>
      <div class="badge" style="font-size:12px">No<br>THC</div>
    </div>
  </section>

</main>
</body>
</html>
```